stationary & business cards for medical clinic
Northfield Institute of Rest Care
stationary & business cards for medical clinic - Medical
Creative Brief
Professional
Delia Marsh
Owner
284 Cobblestone Lane Brookhollow, MS 39402
dmarsh@nirestcare.com
www.nirestcare.com
No color or image on envelope flaps please! No full-bleeds on envelopes or letterhead! Full-bleeds are okay on business cards ONLY.

```html
<!DOCTYPE html>
<html lang="en">
<head>
<meta charset="utf-8">
<title>Northfield Institute of Rest Care – Business Card</title>
<link rel="stylesheet" href="https://fonts.googleapis.com/css2?family=Arimo:wght@400;700&display=swap">
<style>
  :root {
    --backdrop: #2b2b2d;
    --card: #f7f7f7;
    --name-blue: #2f8fd3;
    --ink: #333333;
    --muted: #666666;
    --sky: #3fb6e3;
    --sky-soft: #bfe5f5;
    --mark: #2a7fc7;
  }
  * { box-sizing: border-box; margin: 0; padding: 0; }
  html, body { width: 1200px; height: 901px; overflow: hidden; }
  body {
    background: var(--backdrop);
    font-family: "Arimo", Arial, sans-serif;
    display: flex;
    flex-direction: column;
    align-items: center;
    justify-content: center;
    gap: 50px;
  }
  .card {
    position: relative;
    width: 630px;
    height: 360px;
    background: var(--card);
    border-radius: 8px;
    overflow: hidden;
    box-shadow: 0 8px 24px rgba(0,0,0,.45);
  }
  .brand {
    position: absolute;
    display: flex;
    align-items: center;
    gap: 12px;
  }
  .brand-dot {
    width: 46px; height: 46px;
    border-radius: 50%;
    background: var(--sky);
    flex: none;
  }
  .brand-name {
    color: var(--mark);
    font-weight: 700;
    font-size: 17px;
    line-height: 1.25;
    width: 190px;
  }
  .card-back .brand { left: 200px; top: 150px; }
  .card-front .brand { left: 42px; top: 110px; }
  .contact {
    position: absolute;
    left: 345px;
    top: 40px;
    color: var(--ink);
    font-size: 12px;
    line-height: 1.35;
  }
  .contact-name { color: var(--name-blue); font-size: 21px; font-weight: 400; }
  .contact-role { color: var(--muted); font-size: 12px; margin-bottom: 18px; }
  .contact-address { margin-bottom: 18px; }
  .footer-band {
    position: absolute;
    left: 0; right: 0; bottom: 0;
    height: 100px;
    background: linear-gradient(to bottom, var(--card) 0%, var(--sky-soft) 35%, var(--sky) 100%);
  }
  .website {
    position: absolute;
    right: 50px;
    bottom: 18px;
    color: #ffffff;
    font-size: 12px;
  }
</style>
</head>
<body>
  <section class="card card-back">
    <div class="brand">
      <span class="brand-dot"></span>
      <span class="brand-name">Northfield Institute of Rest Care</span>
    </div>
  </section>

  <section class="card card-front">
    <div class="brand">
      <span class="brand-dot"></span>
      <span class="brand-name">Northfield Institute of Rest Care</span>
    </div>

    <div class="contact">
      <p class="contact-name">Delia Marsh</p>
      <p class="contact-role">Owner</p>
      <p class="contact-address">284 Cobblestone Lane<br>Brookhollow, MS 39402</p>
      <p>T: 866-410-2287</p>
      <p>P: 601-555-0148</p>
      <p>C: 601-555-0172</p>
      <p>F: 601-555-0193</p>
      <p>E: dmarsh@nirestcare.com</p>
    </div>

    <div class="footer-band" role="img" aria-label="Decorative flowing wave stripes in red, navy, white and sky blue along the bottom edge"></div>
    <p class="website">www.nirestcare.com</p>
  </section>
</body>
</html>
```